Business Card Design Project

I have a need for a business card designed. I have a logo.. but need looking for a nice card to go with it. The school is called The Bramblecrest Movement School is the name of the school. Some ideas for what I want on the card.
Guru Reid Pashley
over 25 years martial arts experience
Private and group lessons
kids and adult classes
No contracts or testing fees
styles we teach are escrima, silat, kenpo, and MMA
website is www.bramblecrestms.net
phone is 914-555-0173
visit us on pal net at https://www.palnet.example/pages/The-Bramblecrest-Movement-School/482930175620394

Target Market(s)

adults 1st kids second.

Industry/Entity Type

School

Requirements
Must have
• Guru Reid Pashley
Private and group lessons
phone is 914-555-0173

```html
<!DOCTYPE html>
<html lang="en">
<head>
<meta charset="utf-8">
<title>The Bramblecrest Movement School – Business Card</title>
<link rel="stylesheet" href="https://fonts.googleapis.com/css2?family=Open+Sans:ital,wght@0,300;0,400;0,700;0,800;1,700&display=swap">
<style>
  :root {
    --black: #000000;
    --yellow: #ffff1a;
    --school-yellow: #f4f21c;
    --red-deep: #7a0a00;
    --red: #a81500;
    --orange-glow: #e86a0c;
    --navy: #0f2a8c;
    --white: #ffffff;
    --ink: #111111;
  }
  html, body {
    margin: 0;
    padding: 0;
    width: 1200px;
    height: 868px;
    overflow: hidden;
    background: var(--white);
    font-family: "Open Sans", Arial, sans-serif;
  }
  .canvas { position: relative; width: 1200px; height: 868px; }

  .frame { position: absolute; }
  .frame--black { background: var(--black); }
  .frame--yellow { background: var(--yellow); }

  .card {
    position: absolute;
    overflow: hidden;
    color: var(--white);
    text-align: center;
  }
  .frame--yellow .card { box-shadow: 4px 4px 4px rgba(0,0,0,0.75); }

  /* vertical front */
  .card--front {
    left: 13px; top: 14px; width: 268px; height: 487px;
    background: radial-gradient(ellipse 150px 140px at 50% 110px, var(--orange-glow) 0%, var(--red) 55%, var(--red-deep) 100%);
  }
  .school-name {
    position: absolute; left: 20px; right: 20px;
    margin: 0;
    color: var(--school-yellow);
    font-weight: 800;
    text-transform: uppercase;
    line-height: 1.1;
  }
  .card--front .school-name { top: 110px; font-size: 24px; }
  .styles {
    position: absolute; left: 0; right: 0; top: 238px;
    margin: 0;
    font-size: 27px; font-weight: 700; line-height: 32px;
    letter-spacing: 0.2px;
  }
  .styles small { font-size: 21px; }
  .instructor {
    position: absolute; left: 0; right: 0; top: 315px; height: 56px;
    background: var(--yellow); color: var(--ink);
  }
  .instructor__name { display: block; margin-top: 4px; font-size: 20px; font-weight: 700; }
  .instructor__note { display: block; font-size: 12px; font-weight: 700; font-style: italic; }
  .offerings {
    position: absolute; left: 3px; right: 3px; top: 372px; height: 55px;
    margin: 0; padding: 6px 0 0; list-style: none;
    background: var(--black); border: 1px solid var(--white); box-sizing: border-box;
    font-size: 15.5px; font-weight: 300; line-height: 20px;
  }
  .contact {
    position: absolute; left: 0; right: 0; top: 432px; bottom: 0;
    background: var(--navy);
  }
  .contact__phone { display: block; margin-top: 4px; font-size: 22px; font-weight: 700; line-height: 26px; }
  .contact__web { display: block; font-size: 13px; font-weight: 700; letter-spacing: 0.6px; }

  /* horizontal back */
  .card--back {
    background: linear-gradient(to bottom, var(--red) 0%, var(--red-deep) 55%, var(--red) 100%);
  }
  .frame--black .card--back { outline: 2px solid var(--yellow); outline-offset: -2px; }
  .card--back .school-name { top: 50%; transform: translateY(-50%); font-size: 30px; left: 80px; right: 80px; }
</style>
</head>
<body>
<main class="canvas">

  <section class="frame frame--black" style="left:144px;top:14px;width:294px;height:515px;">
    <div class="card card--front">
      <h1 class="school-name">The Bramblecrest Movement School</h1>
      <p class="styles">ESCRIMA, SILAT,<br>KENPO <small>AND</small> MMA</p>
      <div class="instructor">
        <span class="instructor__name">Guru Reid Pashley</span>
        <span class="instructor__note">over 25 years martial arts experience</span>
      </div>
      <ul class="offerings">
        <li>• Private and Group Lessons</li>
        <li>• No Contracts or Testing Fees</li>
      </ul>
      <div class="contact">
        <span class="contact__phone">914-555-0173</span>
        <span class="contact__web">www.bramblecrestms.net</span>
      </div>
    </div>
  </section>

  <section class="frame frame--yellow" style="left:759px;top:14px;width:294px;height:515px;">
    <div class="card card--front">
      <h1 class="school-name">The Bramblecrest Movement School</h1>
      <p class="styles">ESCRIMA, SILAT,<br>KENPO <small>AND</small> MMA</p>
      <div class="instructor">
        <span class="instructor__name">Guru Reid Pashley</span>
        <span class="instructor__note">over 25 years martial arts experience</span>
      </div>
      <ul class="offerings">
        <li>• Private and Group Lessons</li>
        <li>• No Contracts or Testing Fees</li>
      </ul>
      <div class="contact">
        <span class="contact__phone">914-555-0173</span>
        <span class="contact__web">www.bramblecrestms.net</span>
      </div>
    </div>
  </section>

  <section class="frame frame--black" style="left:35px;top:551px;width:513px;height:294px;">
    <div class="card card--back" style="left:11px;top:11px;width:492px;height:273px;">
      <h2 class="school-name">The Bramblecrest Movement School</h2>
    </div>
  </section>

  <section class="frame frame--yellow" style="left:650px;top:553px;width:511px;height:292px;">
    <div class="card card--back" style="left:12px;top:12px;width:488px;height:269px;">
      <h2 class="school-name">The Bramblecrest Movement School</h2>
    </div>
  </section>

</main>
</body>
</html>
```